Start-up Dog Daycare Needs a Retractable Banner Design for Career Fair

We are a dog daycare located in San Francisco, California, called TailNest Dog Daycare. Our small but dog-knowledgeable team gets to interact with and care for dogs on a daily basis where we supervise playgroups of various sizes. We will like a modern yet fun banner to attract potential new hires and interns. We will like the final design to communicate that we are seeking people who love dogs but who are also hard workers that can thrive in a team setting.

The product specs are as follows:
Document Trim Size - 33.13 X 86.18 inches (84.1 X 218.9cm) with 3312 X 8618 pixels.
Full Bleed Size - 33.38 X 86.43 inches (84.8 X 219.5cm) with 3338 X 8643 pixels.

Additionally, to get a better idea of our brand, attached will be our Company Brand Identity.
Furthermore, attached will be the text we will like included onto our banner.

Target Market(s)

Students at a University

Industry/Entity Type

Pet Care

Font styles to use
Sans Serif

Colors
33a6d7
fbee3e

Requirements
Must have
• Our company logo must be incorporated onto our banner.
• Please include the text in the following order:
• 1. "Dog lovers come talk to us"
• 2. "Internships and full-time positions available"
• Banner Size Specifications:
• Full Bleed Size
• 33.38" x 86.43"
• 84.8 x 219.5 cm
• 3338 x 8643 pixels
• Document Trim Size
• 33.13" x 86.18"
• 84.1 x 218.9 cm
• 3312 x 8618 pixels
• Finished artwork should extend to fill the full bleed area to avoid white edges around.
Nice to have
• - Colors Blue and Yellow
• - Image(s) of a dog(s) playing

```html
<!DOCTYPE html>
<html lang="en">
<head>
<meta charset="utf-8">
<title>TailNest Dog Daycare – Career Fair Banner</title>
<link rel="stylesheet" href="https://fonts.googleapis.com/css2?family=Ubuntu:wght@500;700&display=swap">
<style>
  :root {
    --sky: #86c8e6;
    --brand-blue: #33a6d7;
    --brand-yellow: #fbee3e;
    --band-grey: #f1f1f1;
    --ink: #3d3d3d;
    --white: #ffffff;
  }
  html, body {
    margin: 0;
    padding: 0;
    width: 1200px;
    height: 3123px;
    overflow: hidden;
    background: var(--sky);
  }
  .banner {
    position: relative;
    width: 1200px;
    height: 3123px;
    overflow: hidden;
    font-family: "Ubuntu", "Trebuchet MS", Arial, sans-serif;
  }
  .backdrop {
    position: absolute;
    inset: 0;
    display: block;
  }
  .brand-tab {
    position: absolute;
    left: 323px;
    top: 0;
    width: 510px;
    height: 337px;
    background: var(--white);
    border-radius: 0 0 28px 28px;
    display: flex;
    flex-direction: column;
    align-items: center;
    justify-content: center;
    gap: 20px;
  }
  .brand-dot {
    width: 54px;
    height: 54px;
    border-radius: 50%;
    background: var(--brand-yellow);
  }
  .brand-name {
    margin: 0;
    font-weight: 700;
    font-size: 52px;
    line-height: 1.1;
    color: var(--ink);
    text-align: center;
  }
  .headline {
    position: absolute;
    left: 152px;
    top: 832px;
    margin: 0;
    font-weight: 700;
    font-size: 140px;
    line-height: 146px;
    letter-spacing: 0;
    color: var(--ink);
    text-transform: uppercase;
    white-space: nowrap;
  }
  .headline .accent { color: var(--brand-blue); }
  .openings {
    position: absolute;
    right: 58px;
    top: 2655px;
    margin: 0;
    font-weight: 700;
    font-size: 94px;
    line-height: 108px;
    color: var(--white);
    text-align: right;
    text-transform: uppercase;
    white-space: nowrap;
  }
  .openings .line { display: block; }
  .openings .line.inset { padding-right: 17px; }
  .openings .accent { color: var(--brand-yellow); }
</style>
</head>
<body>
<main class="banner">
  <svg class="backdrop" width="1200" height="3123" viewBox="0 0 1200 3123" xmlns="http://www.w3.org/2000/svg">
    <defs>
      <linearGradient id="lawn" x1="0" y1="0" x2="0" y2="1">
        <stop offset="0" stop-color="#6f8f3a"/>
        <stop offset="0.3" stop-color="#a9cf63"/>
        <stop offset="0.65" stop-color="#93bd4c"/>
        <stop offset="1" stop-color="#6f9a2d"/>
      </linearGradient>
      <radialGradient id="subject-glow" cx="0.5" cy="0.5" r="0.5">
        <stop offset="0" stop-color="#f4efe6" stop-opacity="0.9"/>
        <stop offset="0.6" stop-color="#e8dcc8" stop-opacity="0.55"/>
        <stop offset="1" stop-color="#e8dcc8" stop-opacity="0"/>
      </radialGradient>
      <linearGradient id="puppy" x1="0" y1="0" x2="0" y2="1">
        <stop offset="0" stop-color="#e6c58e"/>
        <stop offset="1" stop-color="#d2a66a"/>
      </linearGradient>
    </defs>

    <rect class="sky-field" x="0" y="0" width="1200" height="3123" fill="var(--sky)"/>

    <g class="play-photo" role="img" aria-label="Photo: a small white and tan terrier running across a sunny lawn with an orange toy bone in its mouth">
      <rect x="0" y="1200" width="1200" height="1450" fill="url(#lawn)"/>
      <ellipse cx="880" cy="1720" rx="300" ry="420" fill="url(#subject-glow)"/>
    </g>

    <path class="band-edge" d="M0,417 C320,417 520,715 1200,730 L1200,1236 C820,1268 420,1575 0,1565 Z" fill="var(--brand-yellow)"/>
    <path class="headline-band" d="M0,490 C320,490 520,740 1200,752 L1200,1198 C820,1230 420,1515 0,1500 Z" fill="var(--band-grey)"/>

    <path class="footer-edge" d="M0,2535 C420,2560 820,2250 1200,2225 L1200,3123 L0,3123 Z" fill="var(--brand-yellow)"/>
    <path class="footer-band" d="M0,2590 C420,2610 820,2290 1200,2262 L1200,3123 L0,3123 Z" fill="var(--brand-blue)"/>

    <rect class="puppy-photo" x="865" y="385" width="240" height="365" rx="110" fill="url(#puppy)"
          role="img" aria-label="Photo: a golden retriever puppy sitting and smiling"/>

    <g class="footer-rule" stroke="var(--white)" stroke-width="3" fill="none" opacity="0.85">
      <line x1="50" y1="3032" x2="560" y2="3032"/>
      <line x1="640" y1="3032" x2="1150" y2="3032"/>
      <circle cx="589" cy="3032" r="10"/>
      <circle cx="611" cy="3032" r="10"/>
    </g>
  </svg>

  <header class="brand-tab">
    <span class="brand-dot"></span>
    <p class="brand-name">TailNest<br>Dog Daycare</p>
  </header>

  <h1 class="headline">Dog lovers<br>come talk<br><span class="accent">to us!</span></h1>

  <p class="openings">
    <span class="line inset">Internships</span>
    <span class="line inset">and full-time</span>
    <span class="line">positions <span class="accent">available!</span></span>
  </p>
</main>
</body>
</html>
```